Valmoric Pocket Folder

Create a new pocket folder
An Overview / Background of the Business & Services
We would like a new folder to use when making formal presentations
* The Target Market / Audience you are trying to reach
The target audience are commercial businesses that we are selling group insurance products to
* Design Specifics; any preferences or ideas for Style, Colour, Imagery, etc
We wanted to use the Houston, Texas skyline and create something that was simple, yet modern.
* Do you have an existing website or Facebook page were designers can learn more about your company?
Yes, http://www.valmoriccorp.example and we are on Linked-In.

```html
<!DOCTYPE html>
<html lang="en">
<head>
<meta charset="utf-8">
<title>Valmoric Pocket Folder</title>
<link rel="stylesheet" href="https://fonts.googleapis.com/css2?family=Open+Sans:wght@400;600&display=swap">
<style>
  :root {
    --backdrop: #d9d9db;
    --panel-light: #f2f3f4;
    --panel-shade: #e1e3e5;
    --brand-blue: #009ddf;
    --brand-blue-deep: #0a8fcc;
    --mark-tint: rgba(170, 200, 215, 0.28);
    --ink-grey: #5a5d61;
    --ink-soft: #8a8d91;
    --card-white: #ffffff;
  }
  * { margin: 0; padding: 0; box-sizing: border-box; }
  html, body { width: 1200px; height: 1000px; overflow: hidden; }
  body {
    background: var(--backdrop);
    font-family: "Open Sans", sans-serif;
    position: relative;
  }
  .folder-spread {
    position: absolute;
    left: 80px; top: 130px;
    width: 1040px; height: 740px;
    display: flex;
    box-shadow: 0 18px 40px rgba(0,0,0,0.18);
  }
  .folder-panel {
    position: relative;
    width: 520px; height: 100%;
    overflow: hidden;
  }
  .folder-panel--left { background: linear-gradient(90deg, var(--panel-shade), var(--panel-light)); }
  .folder-panel--right { background: linear-gradient(90deg, var(--panel-shade), var(--panel-light) 30%); border-left: 1px solid #cfd2d5; }
  .brand-square {
    position: absolute;
    top: 90px;
    width: 440px; height: 440px;
    border-radius: 40px;
    background: var(--mark-tint);
  }
  .folder-panel--left .brand-square { left: 300px; }
  .folder-panel--right .brand-square { left: -220px; }
  .pocket {
    position: absolute;
    bottom: 0; left: 0;
    width: 100%; height: 270px;
    background: linear-gradient(90deg, var(--brand-blue-deep), var(--brand-blue));
  }
  .pocket--left { border-top-right-radius: 26px; }
  .pocket--right { border-top-left-radius: 26px; height: 280px; }
  .business-card {
    position: absolute;
    left: 175px; top: 60px;
    width: 220px; height: 130px;
    background: var(--card-white);
    display: flex;
    align-items: center;
    padding: 0 14px;
    box-shadow: 0 1px 3px rgba(0,0,0,0.2);
  }
  .card-slit { position: absolute; width: 22px; height: 22px; }
  .card-slit--tl { left: -6px; top: -6px; }
  .card-slit--br { right: -6px; bottom: -6px; }
  .card-brand {
    display: flex; align-items: center; gap: 5px;
    font-size: 15px; font-weight: 600; color: var(--ink-grey);
    padding-right: 12px;
    border-right: 1px solid #c8cacc;
    height: 70px;
  }
  .card-brand-dot { width: 10px; height: 10px; background: var(--brand-blue); }
  .card-details { padding-left: 10px; font-size: 5.5px; color: var(--ink-soft); line-height: 1.5; }
  .card-name { font-size: 8px; font-weight: 600; color: var(--ink-grey); }
  .card-role { font-size: 5.5px; margin-bottom: 6px; }
  .card-address { margin-bottom: 6px; }
  .card-contact { display: flex; align-items: center; gap: 3px; }
  .card-contact i { width: 4px; height: 4px; border-radius: 50%; background: var(--brand-blue); display: inline-block; }
</style>
</head>
<body>
  <main class="folder-spread">
    <section class="folder-panel folder-panel--left">
      <div class="brand-square"></div>
      <div class="pocket pocket--left"></div>
    </section>
    <section class="folder-panel folder-panel--right">
      <div class="brand-square"></div>
      <div class="pocket pocket--right">
        <article class="business-card">
          <svg class="card-slit card-slit--tl" viewBox="0 0 22 22"><path d="M0 14 L14 0" stroke="#c8cacc" stroke-width="1.5"/></svg>
          <svg class="card-slit card-slit--br" viewBox="0 0 22 22"><path d="M8 22 L22 8" stroke="#c8cacc" stroke-width="1.5"/></svg>
          <div class="card-brand"><span class="card-brand-dot"></span>Valmoric</div>
          <div class="card-details">
            <div class="card-name">Dorian Vale</div>
            <div class="card-role">President</div>
            <div class="card-address">4200 North Alder Road,<br>Suite 210 Houston, TX 77000</div>
            <div class="card-contact"><i></i>713-555-0142</div>
            <div class="card-contact"><i></i>info@valmoriccorp.example</div>
            <div class="card-contact"><i></i>www.valmoriccorp.example</div>
          </div>
        </article>
      </div>
    </section>
  </main>
</body>
</html>
```